Print materials for 3-star hotel

We are changing up our print materials (notepads, letterheads, key card jackets, small flyer for the room rates) We are a 3 star business hotel in the Philippines and have mainly used grey tones and clean, simple lines. See attached photos for logo and hotel interior photos.

Target Market(s)

Business

Contact Information for Business Card

Corvina Terrace Hotel
Magistrate Lunod Avenue corner Pabilo St Cebu City 6000 Philippines
Tel: +63 32 481 7520
Mobile: +63 917 604 2893
www.corvinaterracehotel.example

Font styles to use
Serif
Sans Serif

Requirements
Must have
• Simple
• Readable font and font size
Nice to have
• Neutral colors, grey and taupes
Should not have
• No purples and bright blues

```html
<!DOCTYPE html>
<html lang="en">
<head>
<meta charset="utf-8">
<title>Corvina Terrace Hotel — Stationery Set</title>
<link href="https://fonts.googleapis.com/css2?family=Cinzel:wght@400&family=Roboto:wght@400;500&display=swap" rel="stylesheet">
<style>
  :root {
    --backdrop: #232323;
    --taupe: #6e655f;
    --taupe-dark: #5e5651;
    --paper: #e6e6e4;
    --card: #f7f7f5;
    --ink: #1c1c1c;
    --brand-ink: #5e5651;
    --light: #efefec;
    --band: #1e1e1e;
  }
  * { box-sizing: border-box; margin: 0; padding: 0; }
  html, body { width: 1200px; height: 1200px; overflow: hidden; }
  body { background: var(--backdrop); position: relative; font-family: "Roboto", Arial, sans-serif; }

  .piece { position: absolute; overflow: hidden; }

  .brand {
    display: flex; align-items: center; justify-content: center; gap: 6px;
    font-family: "Cinzel", Georgia, serif; font-weight: 400;
    letter-spacing: 0.14em; text-transform: uppercase; white-space: nowrap;
  }
  .brand-square { display: inline-block; flex: none; }

  /* Letterhead */
  .letterhead { left: 176px; top: 74px; width: 418px; height: 590px; background: var(--paper); }
  .letterhead-frame { position: absolute; inset: 20px; border: 1.5px solid var(--taupe); }
  .letterhead .brand { position: absolute; top: 62px; left: 0; right: 0; font-size: 11px; color: var(--brand-ink); }
  .letterhead .brand-square { width: 7px; height: 7px; background: var(--brand-ink); }
  .letter-body { position: absolute; left: 84px; width: 280px; top: 130px; font-size: 9.4px; line-height: 11.6px; color: var(--ink); }
  .letter-body p { text-indent: 14px; margin-bottom: 11.6px; }
  .letter-sign-label { position: absolute; left: 104px; top: 455px; font-size: 5.5px; color: var(--ink); }
  .letter-sign-line { position: absolute; left: 240px; top: 460px; width: 64px; border-top: 1px solid var(--ink); }
  .letter-footer { position: absolute; top: 522px; font-size: 5.4px; line-height: 6.6px; color: var(--ink); width: 128px; }
  .letter-footer.left { left: 116px; text-align: justify; }
  .letter-footer.right { left: 274px; text-align: right; }

  /* Notebook */
  .notebook { left: 708px; top: 75px; width: 266px; height: 421px; background: var(--taupe-dark); border-radius: 0 4px 4px 0; }
  .notebook > .brand { position: absolute; top: 100px; left: 0; right: 0; font-size: 11px; color: var(--light); }
  .notebook .brand-square { width: 7px; height: 7px; background: var(--light); }
  .notebook-sleeve { position: absolute; left: 0; right: 0; top: 134px; height: 220px; background: #5a534e; }
  .notebook-sleeve svg { position: absolute; inset: 0; }
  .notebook-sleeve .brand { position: absolute; left: 14px; top: 52px; font-size: 6px; color: #c9c4c0; }
  .notebook-sleeve .brand-square { width: 5px; height: 5px; background: #c9c4c0; }
  .notebook-elastic { position: absolute; top: 0; bottom: 0; left: 236px; width: 7px; background: var(--band); }

  /* Envelope */
  .envelope { left: 708px; top: 550px; width: 440px; height: 226px; background: var(--taupe); }
  .envelope-flap { position: absolute; left: 0; right: 0; top: 0; height: 56px; }
  .envelope-flap-note { position: absolute; right: 14px; top: 22px; width: 150px; font-size: 6px; line-height: 7.5px; color: #555; text-align: right; }
  .envelope-frame { position: absolute; left: 18px; right: 18px; top: 74px; bottom: 18px; border: 1px solid #cfcac6; }
  .envelope .brand { position: absolute; left: 0; right: 0; top: 144px; font-size: 10px; color: var(--light); }
  .envelope .brand-square { width: 7px; height: 7px; background: var(--light); }

  /* Notepad */
  .notepad { left: 190px; top: 736px; width: 208px; height: 296px; background: var(--taupe); }
  .notepad svg { position: absolute; inset: 0; }
  .notepad-binding { position: absolute; left: 0; right: 0; top: 0; height: 10px; background: repeating-linear-gradient(90deg, #111 0 2px, transparent 2px 5px); }
  .notepad .brand { position: absolute; left: 22px; top: 42px; font-size: 6.5px; line-height: 9px; color: var(--light); white-space: normal; gap: 4px; }
  .notepad .brand-name { max-width: 96px; text-align: center; }
  .notepad .brand-square { width: 5px; height: 5px; background: var(--light); }

  /* Mobile screen */
  .screen { left: 485px; top: 774px; width: 101px; height: 154px; background: var(--taupe); }
  .screen .brand { position: absolute; left: 0; right: 0; top: 72px; font-size: 5.6px; letter-spacing: 0.08em; color: var(--light); gap: 3px; }
  .screen .brand-square { width: 4px; height: 4px; background: var(--light); }

  /* Business cards */
  .card { background: var(--card); }
  .card-front { left: 708px; top: 834px; width: 182px; height: 100px; }
  .card-front-frame { position: absolute; inset: 7px 10px; border: 1px solid #8a837e; }
  .card-front .brand { position: absolute; left: 0; right: 0; top: 44px; font-size: 7px; color: var(--brand-ink); gap: 4px; }
  .card-front .brand-square { width: 5px; height: 5px; background: var(--brand-ink); }

  .card-back { left: 708px; top: 990px; width: 180px; height: 100px; }
  .card-back-frame { position: absolute; left: 14px; right: 14px; top: 14px; bottom: 14px; border: 1px solid #777; }
  .card-back .holder { position: absolute; left: 0; right: 0; top: 8px; text-align: center; }
  .card-back .holder span, .card-back .email span { background: var(--card); padding: 0 5px; }
  .card-back .holder span { font-size: 7px; font-weight: 500; letter-spacing: 0.04em; color: #333; }
  .card-back .email { position: absolute; left: 0; right: 0; bottom: 10px; text-align: center; font-size: 6.5px; color: #444; }
  .card-back .side { position: absolute; top: 50px; font-size: 5.5px; color: #444; white-space: nowrap; background: var(--card); padding: 0 3px; }
  .card-back .side.left { left: 14px; transform: translate(-50%, -50%) rotate(-90deg); }
  .card-back .side.right { right: 14px; transform: translate(50%, -50%) rotate(90deg); }
  .card-back .brand { position: absolute; left: 0; right: 0; top: 46px; font-size: 5.6px; letter-spacing: 0.08em; color: #333; gap: 3px; }
  .card-back .brand-square { width: 4px; height: 4px; background: #333; }
</style>
</head>
<body>

  <section class="piece letterhead" aria-label="Letterhead">
    <div class="letterhead-frame"></div>
    <div class="brand"><span class="brand-square"></span>Corvina Terrace Hotel</div>
    <div class="letter-body">
      <p>Lorem ipsum dolor sit amet, consectetur adipiscing elit. Sed auctor feugiat lacus eget pellentesque. Integer purus diam, tincidunt eget ultrices non, tristique ut est. Nullam pellentesque urna non velit elementum vulputate. Phasellus tempor, orci quis sagittis dignissim, elit nibh viverra felis, accumsan rutrum ante leo egestas ligula.</p>
      <p>Nunc rutrum ante sed massa mollis hendrerit. Vivamus sollicitudin, dui a pretium ullamcorper, tellus felis mattis nunc, at rhoncus odio nunc eget risus. Nam fermentum, lorem vel mollis vestibulum, erat metus pulvinar purus, et scelerisque augue nisi sed magna. Duis vehicula vestibulum interdum.</p>
      <p>Curabitur faucibus, nunc nec dignissim vehicula, justo sapien commodo eros, nec tristique elit magna vestibulum nunc.</p>
      <p>Quisque at lacus eget sem aliquam pharetra vel et nulla. Nulla facilisi. Praesent malesuada viverra urna, feugiat tincidunt risus elementum a. Nullam ante enim, ornare quis imperdiet eget, tristique non orci. Praesent velit neque, blandit sed placerat ut, eleifend vitae arcu. Praesent tincidunt viverra nulla at elementum.</p>
    </div>
    <div class="letter-sign-label">Some text here</div>
    <div class="letter-sign-line"></div>
    <div class="letter-footer left">Lorem ipsum dolor sit amet, consectetur adipiscing elit. Sed auctor feugiat lacus eget pellentesque. Integer purus diam, tincidunt eget ultrices non, tristique ut est.</div>
    <div class="letter-footer right">Lorem ipsum dolor sit amet, consectetur adipiscing elit. Sed auctor feugiat lacus eget</div>
  </section>

  <section class="piece notebook" aria-label="Notebook cover">
    <div class="brand"><span class="brand-square"></span>Corvina Terrace Hotel</div>
    <div class="notebook-sleeve">
      <svg width="266" height="220" viewBox="0 0 266 220">
        <polygon points="232,0 250,0 76,220 46,220" fill="#e8e6e3"/>
      </svg>
      <div class="brand"><span class="brand-square"></span>Corvina Terrace Hotel</div>
    </div>
    <div class="notebook-elastic"></div>
  </section>

  <section class="piece envelope" aria-label="Envelope">
    <svg class="envelope-flap" width="440" height="56" viewBox="0 0 440 56">
      <polygon points="0,0 440,0 428,56 12,56" fill="#efefed"/>
    </svg>
    <div class="envelope-flap-note">Lorem ipsum dolor sit amet, consectetur adipiscing elit. Sed auctor feugiat lacus eget</div>
    <div class="envelope-frame"></div>
    <div class="brand"><span class="brand-square"></span>Corvina Terrace Hotel</div>
  </section>

  <section class="piece notepad" aria-label="Notepad cover">
    <svg width="208" height="296" viewBox="0 0 208 296">
      <polygon points="178,20 208,20 208,34 0,275 0,230" fill="#ebebe8"/>
    </svg>
    <div class="notepad-binding"></div>
    <div class="brand"><span class="brand-square"></span><span class="brand-name">Corvina Terrace Hotel</span></div>
  </section>

  <section class="piece screen" aria-label="Mobile splash screen">
    <div class="brand"><span class="brand-square"></span>Corvina Terrace Hotel</div>
  </section>

  <section class="piece card card-front" aria-label="Business card front">
    <div class="card-front-frame"></div>
    <div class="brand"><span class="brand-square"></span>Corvina Terrace Hotel</div>
  </section>

  <section class="piece card card-back" aria-label="Business card back">
    <div class="card-back-frame"></div>
    <div class="holder"><span>LENA ORTIGA</span></div>
    <div class="side left">+63 917 604 2893</div>
    <div class="side right">ADDRESS</div>
    <div class="brand"><span class="brand-square"></span>Corvina Terrace Hotel</div>
    <div class="email"><span>email</span></div>
  </section>

</body>
</html>
```